Redesign the Eshop of a gift shop

We want to redesign the front page, the category page and the product page of our Eshop that sells gifts.
I am thinking not to reveal the url of the eshop as i don't want you to get influenced. Lets call the Eshop "PresentNest.com"
I will list the brands that we resell so you understand what we are selling,
Morvato-https://www.morvato-example.com/
Zandorpel-https://zandorpel-example.com/
Vamtol - https://vamtol-example.com/
Quiet Orchard - https://www.quietorchard-example.com/
Ranger's Workbench - https://rangersworkbench-example.com/
Plumeline press - https://plumelinepress-example.com/
Tarpawn - https://tarpawnofficial-example.com/
We also sell toys for adults like backgamon, chess, playing cards, board games.
The problem is that many eshops sell these and thats why i would like the design to have a different approach, more fresh, not seen before.
I am also thinking of something playfull, happy, but warm at the same time.
Please note that our logo is black & white but feel free to play with any color/s you like in your website design. We might eventually even adjust the logo colors, or you can provide a pallete that suites a black and white logo
Let me know if you have any questions!
Updates
A couple of designers kindly asked to extend so they can submit.
Target Market(s)
Age: 20-50, Gender: Also men but mostly women, Income: Moderate to high, Interests and Lifestyle: Customers who value sentimentality, personal connection, and thoughtful gestures, Relationship Status: Those in relationships or with larger families
Number of Pages Required
3 page
Look and feel
Each slider illustrates characteristics of the customer's brand and the style your logo design should communicate.

```html
<!DOCTYPE html>
<html lang="en">
<head>
<meta charset="utf-8">
<title>PresentNest – Find your unique gifts</title>
<link href="https://fonts.googleapis.com/css2?family=Poppins:wght@400;500;600;700;800;900&display=swap" rel="stylesheet">
<style>
:root{
  --ink:#111111;
  --navy:#0c1624;
  --yellow:#f7c51b;
  --teal:#2fc2b0;
  --red:#e3373a;
  --pink:#efb3b5;
  --soft:#f1f1f1;
  --grey:#777777;
  --white:#ffffff;
}
*{box-sizing:border-box;margin:0;padding:0}
html,body{width:1200px;height:3656px;overflow:hidden}
body{font-family:"Poppins",sans-serif;color:var(--ink);background:var(--white);position:relative}
a{color:inherit;text-decoration:none}

.site-header{position:absolute;top:0;left:0;width:1200px;height:90px;display:flex;align-items:center;justify-content:space-between;padding:0 64px}
.brand{display:flex;align-items:center;gap:10px;font-weight:600;font-size:22px;letter-spacing:.5px}
.brand-box{width:22px;height:22px;background:var(--ink)}
.main-nav{display:flex;align-items:center;gap:40px;font-size:14px;font-weight:600}
.nav-icons{display:flex;gap:18px}
.nav-icons span{width:26px;height:26px;border:2px solid var(--ink);border-radius:50%;display:block}

.hero{position:absolute;top:100px;left:64px;width:1072px;height:532px;background:var(--soft);border-radius:28px;overflow:hidden}
.hero-title{position:absolute;left:62px;top:58px;font-weight:900;font-size:66px;line-height:1.18;text-transform:uppercase}
.hero-title span{display:inline-block;padding:0 10px}
.hl-pink{background:var(--pink)}
.hl-teal{background:var(--teal)}
.hero-sub{position:absolute;left:72px;top:370px;font-size:20px;font-weight:500}
.btn{display:inline-block;background:var(--ink);color:var(--white);font-weight:700;font-size:15px;padding:14px 28px;border-radius:6px}
.hero .btn{position:absolute;left:212px;top:420px}
.hero-dash{position:absolute;left:62px;top:440px;width:100px;height:16px;background:var(--yellow);border-radius:8px;transform:rotate(-6deg)}
.prod{position:absolute;border-radius:40px}

.brand-band{position:absolute;top:676px;left:0;width:1200px;height:112px;background:var(--yellow);display:flex;align-items:center;justify-content:center;gap:70px}
.partner{font-weight:700;font-size:20px;color:var(--ink);text-transform:uppercase}

.section-title{position:absolute;font-weight:800;font-size:30px}
.section-title::after{content:"";position:absolute;left:calc(100% - 30px);bottom:8px;width:60px;height:12px;background:var(--teal);border-radius:6px;transform:rotate(-6deg);z-index:-1}
.new-in{left:64px;top:836px}
.favs{left:64px;top:2270px}
.favs::after{background:var(--yellow)}

.card{position:absolute;border-radius:10px;overflow:hidden}
.card-meta{position:absolute;width:304px;display:flex;justify-content:space-between;align-items:flex-start}
.card-name{font-size:18px;font-weight:600}
.card-tag{font-size:13px;color:var(--grey);margin-top:2px}
.arrow{width:26px;height:20px;margin-top:6px;flex:none}

.outdoors{position:absolute;top:1552px;left:0;width:1200px;height:608px;background:var(--yellow);overflow:hidden}
.out-title{position:absolute;left:668px;top:92px;font-weight:900;font-size:64px;line-height:1;text-transform:uppercase}
.out-title .box{background:var(--white);padding:4px 12px;display:inline-block}
.out-title .the{display:block;font-size:24px;margin:4px 0 -4px 0}
.out-sub{position:absolute;left:676px;top:296px;font-size:21px;font-weight:500;line-height:1.35;width:420px}
.outdoors .btn{position:absolute;left:676px;top:400px}

.fav-card{position:absolute;top:2380px;width:520px;height:360px;border-radius:10px;overflow:hidden}
.fav-word{position:absolute;color:var(--white);font-weight:800;line-height:.95;text-transform:uppercase;white-space:nowrap}

.newsletter{position:absolute;top:2928px;left:0;width:1200px;height:384px;background:var(--pink);text-align:center;color:var(--white)}
.newsletter h2{margin-top:86px;font-weight:800;font-size:36px;line-height:1.25;text-transform:uppercase}
.newsletter p{font-size:20px;margin-top:8px;font-weight:500}
.signup{display:inline-flex;margin-top:24px;background:var(--white);border-radius:6px;padding:6px}
.signup span{width:250px;text-align:left;font-size:14px;color:#999;padding:10px 12px}
.signup b{background:var(--ink);color:var(--white);font-size:15px;padding:10px 22px;border-radius:4px}

.site-footer{position:absolute;top:3312px;left:0;width:1200px;height:344px;background:var(--navy);color:var(--white)}
.foot-brand{position:absolute;left:64px;top:100px}
.foot-brand .brand-box{background:var(--white)}
.foot-tag{position:absolute;left:64px;top:158px;font-size:14px;color:#cfd3d8}
.socials{position:absolute;left:64px;top:196px;display:flex;gap:12px}
.socials span{width:28px;height:28px;background:var(--white);border-radius:50%}
.foot-col{position:absolute;top:96px;font-size:14px}
.foot-col h4{font-weight:600;font-size:16px;margin-bottom:16px}
.foot-col li{list-style:none;color:#cfd3d8;margin-bottom:12px}
</style>
</head>
<body>

<header class="site-header">
  <a class="brand" href="#"><span class="brand-box"></span>PresentNest</a>
  <nav class="main-nav">
    <a href="#">NEW IN</a><a href="#">TOP 50</a><a href="#">CATEGORIES</a><a href="#">BRANDS</a>
    <div class="nav-icons"><span></span><span></span><span></span></div>
  </nav>
</header>

<section class="hero">
  <h1 class="hero-title"><span class="hl-pink">Find</span><br><span>Your</span><br><span class="hl-teal">Unique</span><br><span>Gifts!</span></h1>
  <p class="hero-sub">Unique gifts for unique people.</p>
  <div class="hero-dash"></div>
  <a class="btn" href="#">SHOP NOW</a>
  <div class="prod" role="img" aria-label="Enamel mug with mushroom print" style="left:440px;top:60px;width:150px;height:150px;background:radial-gradient(#f7f2e8,#d9c9a8)"></div>
  <div class="prod" role="img" aria-label="Robot corkscrew" style="left:640px;top:30px;width:130px;height:190px;background:radial-gradient(#d9d9d9,#9a9a9a)"></div>
  <div class="prod" role="img" aria-label="Card wallet in red" style="left:790px;top:140px;width:100px;height:130px;border-radius:12px;background:linear-gradient(#2a2a2a,#c33)"></div>
  <div class="prod" role="img" aria-label="Dog tail bottle stopper" style="left:930px;top:20px;width:90px;height:110px;background:radial-gradient(#e9a463,#c7773b)"></div>
  <div class="prod" role="img" aria-label="Mushroom lamp" style="left:470px;top:270px;width:140px;height:150px;background:radial-gradient(#e0a27a,#a66a47)"></div>
  <div class="prod" role="img" aria-label="Sloth pencil holder" style="left:680px;top:250px;width:150px;height:190px;background:radial-gradient(#c8a882,#8a6a4e)"></div>
  <div class="prod" role="img" aria-label="Pen shaped like a chilli" style="left:880px;top:330px;width:130px;height:70px;transform:rotate(-30deg);background:linear-gradient(90deg,#e3373a,#f0a08a)"></div>
</section>

<section class="brand-band">
  <span class="partner">Morvato</span>
  <span class="partner">Tarpawn</span>
  <span class="partner">Zandorpel</span>
  <span class="partner">Plumeline press</span>
  <span class="partner">Ranger's Workbench</span>
</section>

<h2 class="section-title new-in">NEW IN!</h2>

<div class="card" role="img" aria-label="Mini keyboard gadget on red background" style="left:68px;top:932px;width:304px;height:438px;background:radial-gradient(circle at 50% 45%,#e96a5a,var(--red) 60%)"></div>
<div class="card" role="img" aria-label="Model wearing a striped gauze overall on teal background" style="left:450px;top:932px;width:304px;height:438px;background:radial-gradient(circle at 50% 50%,#d9865e,var(--teal) 55%)"></div>
<div class="card" role="img" aria-label="Cream backpack on pink background" style="left:828px;top:932px;width:304px;height:438px;background:radial-gradient(circle at 50% 45%,#f5eee6,var(--pink) 55%)"></div>

<div class="card-meta" style="left:68px;top:1392px"><div><div class="card-name">Mini Keyboard</div><div class="card-tag">Explore Gifts!</div></div><svg class="arrow" viewBox="0 0 26 20"><path d="M2 10h20M15 3l7 7-7 7" fill="none" stroke="#111" stroke-width="2"/></svg></div>
<div class="card-meta" style="left:450px;top:1392px"><div><div class="card-name">Lumen Tie Gauze Overall</div><div class="card-tag">Explore Clothing!</div></div><svg class="arrow" viewBox="0 0 26 20"><path d="M2 10h20M15 3l7 7-7 7" fill="none" stroke="#111" stroke-width="2"/></svg></div>
<div class="card-meta" style="left:828px;top:1392px"><div><div class="card-name">Pastel Canvas Backpack</div><div class="card-tag">Explore Accessories!</div></div><svg class="arrow" viewBox="0 0 26 20"><path d="M2 10h20M15 3l7 7-7 7" fill="none" stroke="#111" stroke-width="2"/></svg></div>

<section class="outdoors">
  <div class="prod" role="img" aria-label="Canvas hiking backpack" style="left:60px;top:40px;width:200px;height:250px;background:radial-gradient(#4d5a6e,#2b3442)"></div>
  <div class="prod" role="img" aria-label="Camping lantern" style="left:380px;top:30px;width:120px;height:170px;background:radial-gradient(#9aa080,#585e46)"></div>
  <div class="prod" role="img" aria-label="Portable red barbecue grill" style="left:260px;top:270px;width:240px;height:200px;background:radial-gradient(#ee7070,#b72a2d)"></div>
  <div class="prod" role="img" aria-label="Compass" style="left:60px;top:440px;width:100px;height:100px;border-radius:50%;background:radial-gradient(#e8e1d1,#333)"></div>
  <div class="prod" role="img" aria-label="Insulated picnic cooler bag" style="left:960px;top:330px;width:190px;height:190px;background:radial-gradient(#d9dce0,#7c8690)"></div>
  <h2 class="out-title"><span class="box">Explore</span><span class="the">The</span>Outdoors</h2>
  <p class="out-sub">Find the perfect outdoor accessory you never knew you needed!</p>
  <a class="btn" href="#">SHOP NOW</a>
</section>

<h2 class="section-title favs">Mira's Favourite</h2>

<div class="fav-card" style="left:64px;background:var(--teal)">
  <div role="img" aria-label="Reusable mesh produce bags" style="position:absolute;left:160px;top:30px;width:220px;height:200px;border-radius:12px;background:linear-gradient(135deg,#e8a08e,#f0d9a8)"></div>
  <div class="fav-word" style="left:22px;top:140px;font-size:120px">Go</div>
  <div class="fav-word" style="left:22px;top:260px;font-size:66px">Sustainable</div>
</div>
<div class="fav-card" style="left:616px;background:var(--red)">
  <div role="img" aria-label="Yellow spiral notebook" style="position:absolute;left:100px;top:20px;width:170px;height:220px;border-radius:8px;background:linear-gradient(#f7d64a,#e9b92a)"></div>
  <div class="fav-word" style="right:22px;top:150px;font-size:100px">Stop</div>
  <div class="fav-word" style="left:22px;top:260px;font-size:72px">Forgetting</div>
</div>

<div class="card-meta" style="left:64px;top:2756px;width:520px"><div><div class="card-name">Reusable Produce Bags</div><div class="card-tag">Shop Eco-Friendly</div></div><svg class="arrow" viewBox="0 0 26 20"><path d="M2 10h20M15 3l7 7-7 7" fill="none" stroke="#111" stroke-width="2"/></svg></div>
<div class="card-meta" style="left:616px;top:2756px;width:520px"><div><div class="card-name">Everyday Notebook No.12</div><div class="card-tag">Shop Stationery</div></div><svg class="arrow" viewBox="0 0 26 20"><path d="M2 10h20M15 3l7 7-7 7" fill="none" stroke="#111" stroke-width="2"/></svg></div>

<section class="newsletter">
  <h2>Join the PresentNest community!<br>Sign up to our newsletter for deals and more!</h2>
  <p>Type your email down below and receive a discount code.</p>
  <div class="signup"><span>Enter your email here</span><b>SEND</b></div>
</section>

<footer class="site-footer">
  <a class="brand foot-brand" href="#"><span class="brand-box"></span>PresentNest</a>
  <p class="foot-tag">Find your unique gifts!</p>
  <div class="socials"><span></span><span></span><span></span><span></span></div>
  <div class="foot-col" style="left:580px"><h4>Company</h4><ul><li>About</li><li>Contact us</li><li>Support</li><li>Careers</li></ul></div>
  <div class="foot-col" style="left:772px"><h4>Quick Link</h4><ul><li>Delivery Info</li><li>Returns</li><li>Size Guide</li><li>FAQs</li></ul></div>
  <div class="foot-col" style="left:1000px"><h4>Legal</h4><ul><li>Terms &amp; conditions</li><li>Privacy Policy</li><li>Cookie Policy</li></ul></div>
</footer>

</body>
</html>
```